VORELT Diagnostics Pooling One Sheet

The process and concept for pooling is to target large populations of people; i.e. a school, prison, employer (where people are isolated by pods), then to test them all in one controllable group. By breaking down the pool size (ideally is 12 or 16 max) then when a positive pool pops up, the entity has the lab automatically reflex to test the whole pool to determine who is positive. During that exchange, several workflows could take place from the population that was being tested. This type of pooled testing is called Surveillance testing ,when it reflects, then it goes to Screening or Diagnostic testing.

The workflow is:
School/employer collects all patient information captured on a requisition form or electronically (w signature) and DOES NOT send to VORELT
School/employer collects individual specimens and labels them with a unique bar code (non-repeating and can include the DOB)
School/employer is responsible for housing and managing all the unique patient information for each individual specimen
School/employer delivers specimens to VORELT and School/employer directs VORELT what specimens are in what designated pool (one pool size for entire project)
When a pool is positive, VORELT notifies School/employer
When reflex testing in indicated for client, School/employer submits to VORELT on demand all patient information needed to process the reflexed option
VORELT reports back to School/employer in 12 hours the results of the retest
https://www.plaxomer.example/medical-devices/coronavirus-covid-19-and-medical-devices/pooled-sample-testing-and-screening-testing-covid-19
https://www.trunvessa.example/coronavirus-disease-covid-19/news/trunvessa-receives-authorization-covid-19-sample-pooling

Target Market(s)

Schools, Universities, Employers

Font styles to use
Sans Serif

Colors
85acd3
85cae6
34a6d7

Requirements
Must have
• VORELT branded along with an elegant yet clinical feel. have all contact information for VORELT Diagnostics. Go to www.vorelthq.example for all info

```html
<!DOCTYPE html>
<html lang="en">
<head>
<meta charset="utf-8">
<title>VORELT Diagnostics – Pooled Testing</title>
<link href="https://fonts.googleapis.com/css2?family=Montserrat:wght@400;500;600;700;800&display=swap" rel="stylesheet">
<style>
  :root {
    --teal: #2e9db5;
    --teal-deep: #1b5e6c;
    --navy: #2c4452;
    --ink: #2b2f33;
    --rule: #b9c2c7;
    --paper: #ffffff;
    --accent-line: #34a6d7;
  }
  * { margin: 0; padding: 0; box-sizing: border-box; }
  html, body { width: 800px; height: 1200px; overflow: hidden; background: #f2f2f2; }
  body { font-family: "Montserrat", Arial, sans-serif; color: var(--ink); }

  .sheet { position: relative; width: 800px; height: 1200px; background: var(--paper); overflow: hidden; }

  .hex-art { position: absolute; left: 0; top: 0; width: 800px; height: 1200px; }

  .brand { position: absolute; left: 46px; top: 84px; display: flex; align-items: center; gap: 12px; }
  .brand-square { width: 30px; height: 30px; background: var(--navy); }
  .brand-name { font-size: 30px; font-weight: 700; color: var(--navy); letter-spacing: 0.2px; line-height: 34px; }

  .title-band {
    position: absolute; left: 0; top: 177px; width: 371px; height: 283px;
    background: linear-gradient(180deg, var(--teal) 0%, #237f92 55%, var(--teal-deep) 100%);
    padding: 30px 0 0 47px;
  }
  .title-band h1 { font-size: 62px; font-weight: 800; line-height: 66px; color: #fff; letter-spacing: 1px; }
  .title-rule { position: relative; margin-top: 14px; width: 298px; height: 2px; background: rgba(255,255,255,0.85); }
  .title-rule::after { content: ""; position: absolute; left: 22px; top: -2px; width: 36px; height: 5px; background: var(--navy); }
  .title-band .subtitle { margin-top: 28px; font-size: 14.5px; font-weight: 500; line-height: 18px; color: #fff; letter-spacing: 0.3px; }

  .section-head { font-size: 23px; font-weight: 700; color: var(--teal); letter-spacing: 0.5px; line-height: 28px; }
  .section-head .plain { color: var(--navy); font-weight: 500; }
  .head-rule { position: relative; height: 1px; background: var(--rule); margin-top: 10px; }
  .head-rule::after { content: ""; position: absolute; left: 0; top: -1px; width: 26px; height: 3px; background: var(--navy); }

  .strategy { position: absolute; left: 43px; top: 488px; width: 331px; }
  .strategy .head-rule { width: 170px; }
  .strategy p { margin-top: 34px; font-size: 12.6px; line-height: 16.2px; text-align: justify; color: var(--ink); }

  .pool-photo {
    position: absolute; left: 46px; top: 804px; width: 326px; height: 270px;
    border: 3px solid #fff; box-shadow: 0 1px 6px rgba(0,0,0,0.25);
    background: linear-gradient(160deg, #1f7fb0 0%, #39b9e0 45%, #7ad7ef 100%);
  }

  .workflow { position: absolute; left: 424px; top: 620px; width: 350px; }
  .workflow-rule { width: 26px; height: 3px; background: var(--navy); margin-top: 10px; }
  .steps { list-style: none; margin-top: 24px; }
  .steps li { position: relative; padding-left: 30px; font-size: 12.6px; line-height: 15.5px; color: var(--ink); }
  .steps li::before {
    content: ""; position: absolute; left: 3px; top: 3px; width: 9px; height: 9px;
    border: 2px solid var(--navy); border-radius: 50%;
  }
  .steps li + li { margin-top: 15px; }

  .footer-band { position: absolute; left: 0; top: 1120px; width: 800px; height: 80px; }
  .footer-contact { position: absolute; left: 46px; top: 1126px; color: #fff; }
  .footer-contact .phone { display: flex; align-items: center; gap: 8px; font-size: 21px; font-weight: 700; letter-spacing: 0.5px; line-height: 26px; }
  .footer-contact .address { display: flex; align-items: center; gap: 9px; margin-top: 8px; font-size: 12.5px; font-weight: 500; }
  .footer-web { position: absolute; left: 446px; top: 1124px; display: flex; align-items: center; gap: 12px; font-size: 12px; line-height: 16px; color: var(--navy); white-space: nowrap; }
  .footer-web .item { display: flex; align-items: center; gap: 6px; }
</style>
</head>
<body>
<main class="sheet">

  <svg class="hex-art" viewBox="0 0 800 1200">
    <defs>
      <linearGradient id="labTones" x1="0" y1="0" x2="1" y2="1">
        <stop offset="0" stop-color="#b9c3dc"/>
        <stop offset="0.45" stop-color="#5a6fa6"/>
        <stop offset="1" stop-color="#2b3f78"/>
      </linearGradient>
    </defs>
    <g stroke="var(--navy)" stroke-width="11" fill="none">
      <line x1="377" y1="176" x2="377" y2="464"/>
      <line x1="320" y1="146" x2="377" y2="178"/>
      <line x1="377" y1="178" x2="555" y2="75"/>
      <line x1="314" y1="495" x2="377" y2="462"/>
      <line x1="377" y1="462" x2="560" y2="572"/>
      <line x1="613" y1="28" x2="800" y2="136" stroke-width="14"/>
      <line x1="613" y1="600" x2="800" y2="490" stroke-width="14"/>
    </g>
    <polygon role="img" aria-label="Photo: two lab scientists in masks and gloves working at a microscope, with a virus particle illustration"
             points="613,59 827,188 827,446 613,575 399,446 399,188" fill="url(#labTones)"/>
  </svg>

  <div class="brand">
    <span class="brand-square"></span>
    <span class="brand-name">VORELT Diagnostics</span>
  </div>

  <section class="title-band">
    <h1>POOLED<br>TESTING</h1>
    <div class="title-rule"></div>
    <p class="subtitle">POOLED SAMPLE TESTING AND<br>SCREENING TESTING FOR COVID-19</p>
  </section>

  <section class="strategy">
    <h2 class="section-head">STRATEGY</h2>
    <div class="head-rule"></div>
    <p>The process and concept for pooling is to target large populations of people; i.e. a school, prison, employer (where people are isolated by pods), then to test them all in one controllable group. By breaking down the pool size (ideally is 12 or 16 max) then when a positive pool pops up, the entity has the lab automatically reflex to test the whole pool to determine who is positive. During that exchange, several workflows could take place from the population that was being tested. This type of pooled testing is called Surveillance testing, when it reflects, then it goes to Screening or Diagnostic testing.</p>
  </section>

  <div class="pool-photo" role="img" aria-label="Photo: a hand holding a water test kit with coloured vials above a blue swimming pool"></div>

  <section class="workflow">
    <h2 class="section-head"><span class="plain">THE </span>WORKFLOW IS:</h2>
    <div class="workflow-rule"></div>
    <ul class="steps">
      <li>School/employer collects all patient information<br>captured on a requisition form or electronically<br>(w signature) and DOES NOT send to VORELT</li>
      <li>School/employer collects individual specimens<br>and labels them with a unique bar code<br>(non-repeating and can include the DOB)</li>
      <li>School/employer is responsible for housing and<br>managing all the unique patient information for<br>each individual specimen</li>
      <li>School/employer delivers specimens to VORELT<br>and School/employer directs VORELT what<br>specimens are in what designated pool (one<br>pool size for entire project)</li>
      <li>When a pool is positive, VORELT notifies<br>School/employer</li>
      <li>When reflex testing in indicated for client,<br>School/employer submits to VORELT on demand<br>all patient information needed to process the<br>reflexed option</li>
      <li>VORELT reports back to School/employer in 12<br>hours the results of the retest</li>
    </ul>
  </section>

  <svg class="footer-band" viewBox="0 0 800 80" preserveAspectRatio="none">
    <polygon points="0,0 412,0 480,80 0,80" fill="var(--navy)"/>
    <polygon points="466,57 800,57 800,65 473,65" fill="var(--accent-line)"/>
  </svg>

  <div class="footer-contact">
    <div class="phone">
      <svg width="16" height="16" viewBox="0 0 24 24"><path fill="var(--accent-line)" d="M6.6 10.8a15.2 15.2 0 0 0 6.6 6.6l2.2-2.2c.3-.3.7-.4 1-.2 1.1.4 2.3.6 3.6.6.6 0 1 .4 1 1V20c0 .6-.4 1-1 1C10.6 21 3 13.4 3 4c0-.6.4-1 1-1h3.5c.6 0 1 .4 1 1 0 1.3.2 2.5.6 3.6.1.3 0 .7-.2 1z"/></svg>
      844-800-VORELT (86735)
    </div>
    <div class="address">
      <svg width="12" height="16" viewBox="0 0 12 16"><path fill="var(--accent-line)" d="M6 0a6 6 0 0 0-6 6c0 4.5 6 10 6 10s6-5.5 6-10a6 6 0 0 0-6-6zm0 8.5A2.5 2.5 0 1 1 6 3.5a2.5 2.5 0 0 1 0 5z"/></svg>
      1180 Meridian Court Suite I Halvern, MD 20999
    </div>
  </div>

  <div class="footer-web">
    <span class="item">
      <svg width="14" height="10" viewBox="0 0 14 10"><rect x="0.5" y="0.5" width="13" height="9" fill="none" stroke="var(--accent-line)"/><path d="M0.5 0.5 7 5.5 13.5 0.5" fill="none" stroke="var(--accent-line)"/></svg>
      info@vorelthq.example
    </span>
    <span class="item">
      <svg width="12" height="12" viewBox="0 0 12 12"><circle cx="6" cy="6" r="5.3" fill="none" stroke="var(--accent-line)" stroke-width="1.2"/><ellipse cx="6" cy="6" rx="2.3" ry="5.3" fill="none" stroke="var(--accent-line)"/><line x1="0.7" y1="6" x2="11.3" y2="6" stroke="var(--accent-line)"/></svg>
      www.vorelthq.example
    </span>
  </div>

</main>
</body>
</html>
```